Community coffee table book/quiz book

I need a couple of things for my book:
- Book cover (Title: "1000 spørsmål om Kvernlia")
- "Cover pages" for each chapter of the book (15-16 chapters)
- "Watermark" or background design for all the pages of the book.
- A cover image for the book's Kettlebook page.
- Design of a paper "belt"

The book:
The book will consist of about 200+ pages with ten questions on one page and ten answers on the next.

The name of the book is "1000 spørsmål om Kvernlia" which means 1000 questions about Fyllingsdalen (Fyllingsdalen is a suburb of the city Bergen in Norway). Author is Tore Halvik.
The questions in the book are grouped in chapters like:
History
Facts
Schools
Businesses
People/profiles
Sport
Culture
Buildings/Landmarks/Sculptures
The different areas of the suburb
The city
Language/expressions
Nature
The names of the chapters are not set, so it would be good to have the option to change the title of the pages without having to contact the designer (maybe by adding the text on top of the cover page?). I therefore suggest that these images are without text.
The book size is 18X18 cm.

The chapter cover pages:
The book will basically consist of text. Ten questions on one page, and ten questions on the next. Visually it will be quite "boring" to look at. I would therefore like to have a chapter cover page for each chapter, preferable in colour.

Water mark:
To avoid having a book full of white pages with limited amount of text I thought of having some kind of design on each page. I do not know how this should be done, but maybe it is possible to create some kind of background image or watermark image with similar design as the book cover and the chapter covers?

The Kettlebook cover image:
This should be the same as, or similar to, the book cover.
I believe the optimal size is 828px x 315px?

Paper "belt":
The book is to be sold for charity. The receiver of the money is the local sports club. I would like to have the book "wrapped in a 5-6 cm wide paper belt with the logo of the sports club (please see logo and colours here: http://www.ilbrattmo.example). I do not think that the book cover itself should have the sports club's color (purple), but maybe the paper band could? (Again: YOU are the designer)

Photos:
I reckon you would like some photos for both the book cover and the chapter covers. I will of course do the best I can to provide these photos when I have selected a designer. I the meantime

Target Market(s)

Target market is middle clas men and women 35+ from the geographical area Fyllingsdalen.

Industry/Entity Type

Community

Font styles to use
Serif
Sans Serif

Requirements
Must have
• The book will be sold by children on doors. The buyers will probably take a look briefly through the book and then decide if they are going to buy.
• It is important that they like the question types, categories and some of the actual questions they read. But it is also important that they like the look of the book. Therefore the book cover and the chapter cover pages must be appealing enough for the buyers to want this book on theor coffee table.
Nice to have
• I have uploaded a short video clip to VidPlaza (https://www.vidplaza.example/watch?v=qoz4Tr7wnLx). This a promo clip from Pimbo Kanal. I felt inspired when I saw it and thought that backgrounds like the ones used in the promo could also be used as backgrounds for each chapter's cover pages. Maybe different colour for each chapter? Screenshots from the clip is uploaded below.
• Then again: Maybe I am an idiot? YOU are the designer :-)
Should not have
• There has been some rivalry between two sportsclubs in the region after the clubs was merged a couple of years ago. I therefore believe we should therefore try avoid both the old clubs' colours (blue&yellow and green) and the new club's colour (purple).

```html
<!DOCTYPE html>
<html lang="no">
<head>
<meta charset="utf-8">
<title>1000 spørsmål om Kvernlia – design board</title>
<link rel="stylesheet" href="https://fonts.googleapis.com/css2?family=Instrument+Serif&family=Poppins:wght@600;700;800&display=swap">
<style>
  :root {
    --board: #000000;
    --label: #ffffff;
    --red: #ed1c24;
    --orange: #f26522;
    --white: #ffffff;
    --belt-purple: #382a75;
    --belt-blue: #7f9fcf;
    --photo-light: #d9d9d9;
    --photo-mid: #8a8a8a;
    --photo-dark: #3a3a3a;
  }
  * { margin: 0; padding: 0; box-sizing: border-box; }
  html, body { width: 1200px; height: 2571px; overflow: hidden; }
  body { background: var(--board); position: relative; font-family: "Poppins", sans-serif; }

  .section-label {
    position: absolute; left: 0; width: 1200px; text-align: center;
    font-family: "Instrument Serif", serif; font-size: 64px; line-height: 1;
    color: var(--label); letter-spacing: -1px;
  }

  .photo {
    position: absolute;
    background: linear-gradient(180deg, var(--photo-light) 0%, var(--photo-mid) 45%, var(--photo-dark) 70%, var(--photo-mid) 100%);
    clip-path: polygon(4% 22%, 10% 12%, 22% 14%, 30% 4%, 48% 8%, 60% 2%, 74% 6%, 86% 3%, 92% 14%, 90% 30%, 100% 44%, 94% 58%, 98% 72%, 88% 80%, 80% 96%, 62% 92%, 46% 100%, 30% 94%, 18% 98%, 10% 86%, 6% 70%, 0% 56%, 6% 44%, 2% 32%);
  }
  .question-mark {
    position: absolute; font-family: "Poppins", sans-serif; font-weight: 800;
    color: var(--white); opacity: .85; line-height: 1;
  }

  .title { position: absolute; color: var(--white); transform: rotate(-5deg); transform-origin: left bottom; }
  .title-lead { display: block; font-weight: 700; line-height: 1; }
  .title-place {
    display: inline-block; font-weight: 800; line-height: 1;
    border-bottom: solid var(--white); padding-bottom: 2px;
  }

  /* Cover */
  .cover {
    position: absolute; left: 324px; top: 123px; width: 571px; height: 571px; overflow: hidden;
    background: linear-gradient(30deg, var(--red) 0%, var(--orange) 100%);
  }
  .cover .photo { left: 62px; top: 39px; width: 454px; height: 274px; }
  .cover .question-mark { left: 214px; top: 16px; font-size: 300px; }
  .cover .title { left: 53px; top: 325px; }
  .cover .title-lead { font-size: 30px; }
  .cover .title-place { font-size: 70px; border-bottom-width: 9px; }
  .cover .author {
    position: absolute; right: 24px; bottom: 24px; color: var(--white);
    font-weight: 700; font-size: 14px;
  }

  /* Belt */
  .belt {
    position: absolute; left: 324px; top: 857px; width: 571px; height: 177px;
    background: var(--belt-blue); display: flex; align-items: center;
  }
  .belt-band { width: 151px; height: 100%; background: var(--belt-purple); border-right: 3px solid var(--white); }
  .belt-club { display: flex; align-items: center; gap: 10px; margin-left: -18px; }
  .belt-mark { width: 40px; height: 40px; border-radius: 50%; background: var(--belt-purple); }
  .belt-name { color: var(--white); font-weight: 700; font-size: 26px; letter-spacing: .5px; }

  /* Watermarked page */
  .page { position: absolute; left: 321px; top: 1214px; width: 574px; height: 574px; background: var(--white); }
  .page .photo { left: 9px; top: 480px; width: 130px; height: 72px; opacity: .35; }

  /* Social cover */
  .social-cover {
    position: absolute; left: 211px; top: 1980px; width: 799px; height: 297px; overflow: hidden;
    background: linear-gradient(80deg, var(--red) 0%, var(--orange) 100%);
  }
  .social-cover .photo { left: 329px; top: 17px; width: 446px; height: 257px; }
  .social-cover .question-mark { left: 508px; top: 10px; font-size: 270px; }
  .social-cover .title { left: 21px; top: 90px; }
  .social-cover .title-lead { font-size: 25px; }
  .social-cover .title-place { font-size: 56px; border-bottom-width: 7px; }
</style>
</head>
<body>
  <h2 class="section-label" style="top:54px">Cover Design</h2>
  <section class="cover">
    <div class="photo" role="img" aria-label="Black and white harbour view of the town with houses and hills reflected in water"></div>
    <span class="question-mark">?</span>
    <h1 class="title"><span class="title-lead">1000 spørsmål om</span><span class="title-place">Kvernlia</span></h1>
    <p class="author">Tore Halvik.</p>
  </section>

  <h2 class="section-label" style="top:758px">Paper Belt Design</h2>
  <section class="belt">
    <div class="belt-band"></div>
    <div style="flex:1; display:flex; justify-content:center;">
      <div class="belt-club"><span class="belt-mark"></span><span class="belt-name">IL BRATTMO</span></div>
    </div>
  </section>

  <h2 class="section-label" style="top:1112px">Watermarked Page</h2>
  <section class="page">
    <div class="photo" role="img" aria-label="Faint harbour view watermark"></div>
  </section>

  <h2 class="section-label" style="top:1876px">Kettlebook Cover Photo</h2>
  <section class="social-cover">
    <div class="photo" role="img" aria-label="Black and white harbour view of the town with houses and hills reflected in water"></div>
    <span class="question-mark">?</span>
    <h1 class="title"><span class="title-lead">1000 spørsmål om</span><span class="title-place">Kvernlia</span></h1>
  </section>
</body>
</html>
```